Estate Agent/Real Estate valuation tool

We need a design for our our new estate agent valuation tool.

The tool allows users to book a valuation of their house/property with the estate agent, after they choose there property they can then complete their details and choose a booking time.

The mock up of the design we want is attached to this project.(Main Screen)

This also needs to be responsive so the design is easy to use on a mobile device.

Target Market(s)

Harbourline Homes

Industry/Entity Type

Real Estate Agent

Number of Pages Required

1 page

Requirements
Must have
• Section 2 and 3 greyed out when user is on step 1
• Section 1 and 3 greyed out when user is on step 2
• Section 1 and 2 greyed out when the user is on step 3
• *** Design must be shown for mobile/ipad and desktop
Nice to have
• Clean and Simple
Should not have
• Dark colours

```html
<!DOCTYPE html>
<html lang="en">
<head>
<meta charset="UTF-8">
<title>Harbourline Homes – Book Your Valuation Online</title>
<link href="https://fonts.googleapis.com/css2?family=Cinzel:wght@400;500&family=Raleway:wght@400;500&display=swap" rel="stylesheet">
<style>
  :root {
    --sky-top: #c9d8ec;
    --sky-mid: #9db6d8;
    --water: #7f9fc9;
    --land: #7b9a78;
    --brand-blue: #1aa6e6;
    --brand-dark: #1d1d1f;
    --tagline: #7b8fd3;
    --property: #ef3e68;
    --property-line: #e8335e;
    --details: #cdc1e8;
    --details-line: #8c6cc6;
    --appointment: #b6e3c9;
    --appointment-line: #34b56a;
    --panel-body: rgba(244, 246, 249, 0.9);
    --field-bg: rgba(255, 255, 255, 0.55);
    --field-border: #d4d8de;
    --field-text: #a9adb3;
    --button-dark: #2d2d2d;
    --button-muted: #b3b3b3;
    --tab-bg: #bfe6d0;
    --tab-text: #8fa89a;
    --tab-active: #b3b3b3;
    --footer: #29b6f0;
    --white: #ffffff;
  }
  * { box-sizing: border-box; margin: 0; padding: 0; }
  html, body { width: 1200px; height: 562px; overflow: hidden; }
  body { font-family: "Raleway", sans-serif; }

  .canvas { position: relative; width: 1200px; height: 562px; overflow: hidden; }

  .backdrop {
    position: absolute; inset: 0;
    background:
      radial-gradient(ellipse 320px 200px at 600px 90px, rgba(255,255,255,0.85), rgba(255,255,255,0) 70%),
      linear-gradient(90deg, rgba(150,175,210,0.7) 0, rgba(150,175,210,0) 22%),
      linear-gradient(180deg, var(--sky-top) 0%, var(--sky-mid) 55%, var(--water) 78%, var(--land) 100%);
  }

  .brand { position: absolute; left: 454px; top: 12px; width: 290px; text-align: center; }
  .brand-mark { display: block; margin: 0 auto 4px; }
  .brand-name {
    display: block;
    border-top: 2px solid var(--brand-blue);
    border-bottom: 2px solid var(--brand-blue);
    font-family: "Cinzel", serif; font-size: 32px; line-height: 34px;
    color: var(--brand-blue); letter-spacing: 1px;
  }
  .tagline {
    position: absolute; left: 0; width: 1200px; top: 106px; text-align: center;
    font-family: "Cinzel", serif; font-size: 23px; color: var(--tagline); letter-spacing: 1px;
  }

  .step {
    position: absolute; top: 160px; width: 270px; height: 310px;
    background: var(--panel-body); border-radius: 3px; overflow: hidden;
  }
  .step-title {
    height: 38px; line-height: 38px; text-align: center;
    color: var(--white); font-size: 19px; letter-spacing: 0.3px;
  }
  .step-property { left: 162px; border-bottom: 3px solid var(--property-line); }
  .step-property .step-title { background: var(--property); }
  .step-details { left: 465px; border-bottom: 3px solid var(--details-line); }
  .step-details .step-title { background: var(--details); }
  .step-appointment { left: 770px; border-bottom: 3px solid var(--appointment-line); }
  .step-appointment .step-title { background: var(--appointment); }

  .field {
    position: absolute; left: 15px; width: 238px; height: 32px;
    border: 1px solid var(--field-border); border-radius: 3px; background: var(--field-bg);
    padding-left: 11px; line-height: 30px; font-size: 13px; color: var(--field-text);
  }
  .postcode { width: 156px; background: var(--white); color: #333; border-radius: 3px 0 0 3px; }
  .search-button {
    position: absolute; left: 170px; top: 65px; width: 84px; height: 32px;
    background: var(--button-dark); color: var(--white); border-radius: 0 3px 3px 0;
    text-align: center; line-height: 32px; font-size: 14px;
  }
  .button {
    position: absolute; height: 32px; border-radius: 3px; text-align: center;
    line-height: 32px; font-size: 15px; color: var(--white);
  }
  .button-proceed { left: 60px; top: 252px; width: 140px; }
  .button-dark { background: var(--button-dark); }
  .button-muted { background: var(--button-muted); border: 1px solid #a9a9a9; }

  .day-tabs { position: absolute; left: 15px; top: 54px; display: flex; gap: 5px; }
  .day-tab {
    width: 30px; height: 29px; border-radius: 2px; background: var(--tab-bg);
    border: 1px solid #a9d9bd; color: var(--tab-text);
    font-size: 7px; line-height: 8px; text-align: center;
    display: flex; align-items: center; justify-content: center;
  }
  .day-tab.is-selected { background: var(--tab-active); border-color: #999; color: #eee; }

  .slots { position: absolute; left: 15px; top: 89px; }
  .slot { display: flex; height: 29px; margin-bottom: 5.5px; border-radius: 3px; overflow: hidden; border: 1px solid var(--field-border); }
  .slot-date { width: 185px; background: var(--field-bg); color: #a3a7ad; font-size: 13px; line-height: 27px; padding-left: 9px; }
  .slot-time { width: 52px; background: var(--button-muted); color: var(--white); font-size: 13px; line-height: 27px; text-align: center; }
  .button-confirm { left: 60px; top: 266px; width: 140px; }

  .footer {
    position: absolute; left: 0; top: 520px; width: 1200px; height: 42px;
    background: var(--footer); color: var(--white);
  }
  .copyright { position: absolute; left: 163px; top: 14px; font-size: 12px; }
  .social { position: absolute; left: 872px; top: 5px; display: flex; gap: 12px; list-style: none; }
  .social-link {
    width: 32px; height: 32px; border-radius: 50%; border: 2px solid #d9eef8;
    background: #e9f5fb;
  }
</style>
</head>
<body>
<main class="canvas">
  <div class="backdrop" role="img" aria-label="Soft sky-blue photograph of a waterfront high-rise apartment tower and city skyline"></div>

  <header class="brand">
    <svg class="brand-mark" width="14" height="14" viewBox="0 0 14 14" aria-hidden="true"><rect width="14" height="14" fill="var(--brand-blue)"/></svg>
    <span class="brand-name">Harbourline Homes</span>
  </header>
  <h1 class="tagline">Book Your Valuation Online</h1>

  <section class="step step-property">
    <h2 class="step-title">PROPERTY DETAILS</h2>
    <div class="field postcode" style="top:65px">Postcode</div>
    <div class="search-button">Search</div>
    <div class="field" style="top:110px">Street</div>
    <div class="field" style="top:154px">City</div>
    <div class="field" style="top:199px">Country</div>
    <div class="button button-proceed button-dark">Proceed</div>
  </section>

  <section class="step step-details">
    <h2 class="step-title">YOUR DETAILS</h2>
    <div class="field" style="top:65px">Name</div>
    <div class="field" style="top:110px">Email</div>
    <div class="field" style="top:154px">Number</div>
    <div class="button button-proceed button-muted">Proceed</div>
  </section>

  <section class="step step-appointment">
    <h2 class="step-title">APPOINTMENT TIME</h2>
    <div class="day-tabs">
      <div class="day-tab">Today</div>
      <div class="day-tab is-selected">Tomo-<br>rrow</div>
      <div class="day-tab">Mon<br>30th</div>
      <div class="day-tab">Tue<br>01st</div>
      <div class="day-tab">Wed<br>02st</div>
      <div class="day-tab">Thurs<br>04st</div>
      <div class="day-tab">Fri<br>05tht</div>
    </div>
    <div class="slots">
      <div class="slot"><span class="slot-date">Sunday 29th November</span><span class="slot-time">08 : 30</span></div>
      <div class="slot"><span class="slot-date">Sunday 29th November</span><span class="slot-time">10 : 30</span></div>
      <div class="slot"><span class="slot-date">Sunday 29th November</span><span class="slot-time">12 : 30</span></div>
      <div class="slot"><span class="slot-date">Sunday 29th November</span><span class="slot-time">14 : 30</span></div>
      <div class="slot"><span class="slot-date">Sunday 29th November</span><span class="slot-time">16 : 30</span></div>
    </div>
    <div class="button button-confirm button-muted">Confrim Booking</div>
  </section>

  <footer class="footer">
    <p class="copyright">Northgate Web Studio Ltd. All rights reserved.</p>
    <ul class="social">
      <li class="social-link" aria-label="Social profile 1"></li>
      <li class="social-link" aria-label="Social profile 2"></li>
      <li class="social-link" aria-label="Social profile 3"></li>
      <li class="social-link" aria-label="Social profile 4"></li>
    </ul>
  </footer>
</main>
</body>
</html>
```